Your complete Gardening and lawn maintenance, Horticultural care. (to be on card)
We are looking at using a logo of a tree, with a recycling emblem circling the tree. The colors of choice, are burnt oranges and olive greens. Presented; simple to the eye, yet catchy to the clients in a eco-friendly way. We have uploaded a design for you to look at just to give a rough idea, you can use that or create your own ideas or play around with a mixture.

Target Market(s)

Home owners, businesses, real estates.

Industry/Entity Type

Recycling

Contact Information for Business Card

Name: Colin Breversted
Phone: 0438159027
Email: brightmossyards@mailbarn.net

Logo Text

Bright-Moss Yards

Logo styles of interest
Emblem Logo
Pictorial/Combination Logo
Abstract Logo
Requirements
Must have
• Business name: Bright-Moss Yards
and slogan : Your complete Gardening and lawn maintenance, Horticultural care

```html
<!DOCTYPE html>
<html lang="en">
<head>
<meta charset="utf-8">
<title>Bright-Moss Yards – Business Card</title>
<link rel="stylesheet" href="https://fonts.googleapis.com/css2?family=Exo+2:wght@300;400;500;700;800&display=swap">
<style>
  :root {
    --paper: #ffffff;
    --ink-border: #111111;
    --burnt-orange: #ff4a0a;
    --olive: #9a995c;
    --olive-text: #8f8e58;
    --band-text: #ffffff;
  }
  * { margin: 0; padding: 0; box-sizing: border-box; }
  html, body {
    width: 1200px;
    height: 741px;
    overflow: hidden;
    background: var(--paper);
    font-family: "Exo 2", sans-serif;
  }
  .card {
    position: absolute;
    left: 26px;
    top: 38px;
    width: 1148px;
    height: 663px;
    border: 2px solid var(--ink-border);
    border-radius: 38px;
    overflow: hidden;
    background: var(--paper);
  }
  .contact {
    position: absolute;
    right: 62px;
    top: 92px;
    text-align: right;
  }
  .contact__name {
    font-size: 54px;
    font-weight: 400;
    color: var(--burnt-orange);
    letter-spacing: 1px;
    line-height: 1;
  }
  .contact__phone {
    margin-top: 20px;
    font-size: 28px;
    font-weight: 500;
    color: var(--olive-text);
    line-height: 1.1;
  }
  .contact__email {
    font-size: 28px;
    font-weight: 300;
    color: var(--olive-text);
    line-height: 1.1;
  }
  .brand-mark {
    position: absolute;
    left: 74px;
    top: 212px;
    width: 260px;
    height: 260px;
  }
  .brand-name {
    position: absolute;
    left: 72px;
    top: 478px;
    font-size: 52px;
    font-weight: 800;
    letter-spacing: 5px;
    text-transform: uppercase;
    color: var(--olive);
    line-height: 1;
    white-space: nowrap;
  }
  .slogan-band {
    position: absolute;
    left: 0;
    right: 0;
    bottom: 0;
    height: 113px;
    background: var(--olive);
  }
  .slogan {
    position: absolute;
    left: 74px;
    top: 4px;
    font-size: 29px;
    font-weight: 400;
    color: var(--band-text);
    white-space: nowrap;
  }
</style>
</head>
<body>
  <main class="card">
    <section class="contact">
      <p class="contact__name">Colin Breversted</p>
      <p class="contact__phone">T: 0438159027</p>
      <p class="contact__email">E: brightmossyards@mailbarn.net</p>
    </section>

    <svg class="brand-mark" viewBox="0 0 260 260" aria-hidden="true">
      <circle cx="130" cy="130" r="118" fill="none" stroke="var(--burnt-orange)" stroke-width="14"/>
    </svg>

    <h1 class="brand-name">Bright-Moss Yards</h1>

    <footer class="slogan-band">
      <p class="slogan">Your complete Gardening and lawn maintenance, Horticultural care</p>
    </footer>
  </main>
</body>
</html>
```